Design Business Card
Business Card
Design Business Card -
Creative Brief
Simple
GlowNest by Beam
Let the radiant you bloom anew...
4875 Carling Ave. Suite #216 Westhaven, CA 94077
bivorapelt@mailvex.net
www.glownestbybeam.net
web address is not confirmed yet; website is currently under construction. Please match coloring and concept to the logo we selected.
Appointment For:__________________ Date:_________________ Time:_________________ If you are unable to keep your appointment, please kindly give 24 hours advanced notice. $100 will be charged for cancellations/reschedules without 24 hours notice. $200 will be charged for no-shows per appointment.

```html
<!DOCTYPE html>
<html lang="en">
<head>
<meta charset="utf-8">
<title>GlowNest by Beam — Business Card</title>
<link rel="stylesheet" href="https://fonts.googleapis.com/css2?family=Open+Sans:wght@400;600&display=swap">
<style>
  :root {
    --backdrop: #e9559f;
    --card: #fbfafb;
    --magenta: #c4157a;
    --ink: #3a3a3a;
    --rule: #d63a92;
  }
  html, body {
    margin: 0;
    width: 1200px;
    height: 901px;
    overflow: hidden;
    background: var(--backdrop);
    font-family: "Open Sans", Arial, sans-serif;
  }
  .stage {
    width: 1200px;
    height: 901px;
    display: flex;
    align-items: center;
    justify-content: center;
    gap: 40px;
  }
  .card {
    position: relative;
    width: 540px;
    height: 310px;
    background: var(--card);
    box-shadow: 0 6px 18px rgba(90, 0, 50, 0.25);
    overflow: hidden;
    color: var(--ink);
  }
  .card-lines {
    position: absolute;
    inset: 0;
    width: 100%;
    height: 100%;
  }
  .brand {
    position: absolute;
    left: 32px;
    top: 30px;
    margin: 0;
    font-size: 28px;
    font-weight: 400;
    color: var(--magenta);
    letter-spacing: -0.5px;
  }
  .tagline {
    position: absolute;
    right: 28px;
    top: 58px;
    margin: 0;
    font-size: 12px;
    color: var(--ink);
  }
  .website {
    position: absolute;
    right: 28px;
    bottom: 24px;
    margin: 0;
    font-size: 13px;
    color: var(--magenta);
  }
  .contact {
    position: absolute;
    left: 32px;
    bottom: 30px;
    margin: 0;
    font-style: normal;
    font-size: 13px;
    line-height: 1.45;
  }
  .appointment {
    position: absolute;
    left: 32px;
    top: 96px;
    width: 230px;
    font-size: 12px;
    line-height: 1.9;
  }
  .appointment .field {
    display: flex;
    gap: 6px;
  }
  .appointment .field span.blank {
    flex: 1;
    border-bottom: 1px solid var(--ink);
    margin-bottom: 6px;
  }
  .policy {
    position: absolute;
    left: 32px;
    bottom: 26px;
    width: 330px;
    margin: 0;
    font-size: 10px;
    line-height: 1.45;
  }
</style>
</head>
<body>
<main class="stage">
  <section class="card card-back" aria-label="Appointment card">
    <svg class="card-lines" viewBox="0 0 540 310" aria-hidden="true">
      <g stroke="var(--rule)" stroke-width="1.6" fill="none">
        <line x1="300" y1="22" x2="540" y2="22"/>
        <line x1="320" y1="32" x2="540" y2="32"/>
        <line x1="340" y1="42" x2="540" y2="42"/>
        <line x1="360" y1="80" x2="540" y2="80"/>
        <line x1="490" y1="92" x2="490" y2="270"/>
        <line x1="502" y1="92" x2="502" y2="270"/>
        <line x1="514" y1="92" x2="514" y2="270"/>
      </g>
    </svg>
    <h2 class="brand">GlowNest by Beam</h2>
    <p class="tagline">Let the radiant you bloom anew...</p>
    <div class="appointment">
      <div>Appointment</div>
      <div class="field">For: <span class="blank"></span></div>
      <div class="field">Date: <span class="blank"></span></div>
      <div class="field">Time: <span class="blank"></span></div>
    </div>
    <p class="policy">If you are unable to keep your appointment, please kindly give 24 hours advanced notice. $100 will be charged for cancellations/reschedules without 24 hours notice. $200 will be charged for no-shows per appointment.</p>
    <p class="website">www.glownestbybeam.net</p>
  </section>

  <section class="card card-front" aria-label="Contact card">
    <svg class="card-lines" viewBox="0 0 540 310" aria-hidden="true">
      <g stroke="var(--rule)" stroke-width="1.6" fill="none">
        <line x1="300" y1="22" x2="540" y2="22"/>
        <line x1="320" y1="32" x2="540" y2="32"/>
        <line x1="340" y1="42" x2="540" y2="42"/>
        <line x1="360" y1="80" x2="540" y2="80"/>
        <line x1="490" y1="92" x2="490" y2="270"/>
        <line x1="502" y1="92" x2="502" y2="270"/>
        <line x1="514" y1="92" x2="514" y2="270"/>
      </g>
    </svg>
    <h2 class="brand">GlowNest by Beam</h2>
    <p class="tagline">Let the radiant you bloom anew...</p>
    <address class="contact">
      4875 Carling Ave. Suite #216<br>
      Westhaven, CA 94077<br>
      Phone: 415.555.0142<br>
      Fax: 415.555.0187<br>
      E-mail: bivorapelt@mailvex.net
    </address>
    <p class="website">www.glownestbybeam.net</p>
  </section>
</main>
</body>
</html>
```